Outdoor Company Business Card design

We are an outdoor adventure company needing a business card. We sell outdoor adventures and clothing. Please use our logo in the business card. We are looking for something unique but delivers a clear message as to who we are. Please be creative

Target Market(s)

Outdoor adventures

Industry/Entity Type

Business

Contact Information for Business Card

Business name: TrailBirch If using the logo, no need to have a spot for the name
Owner / CEO: Ross Dalby
Website: TrailBirch.example
FriendLoop: FriendLoop.example/TrailBirch
Instagram: @dalby_ross
phone number: 555-304-7192
Email: Dalbycrew@TrailBirch.example

Colors

Designer to choose colors to be used in the design.

Requirements
Must have
• The business card must include the details mentioned above. ie logo, my name, email, facebook, instagram, website, and phone number.
Should not have
• should not be cluttered or look messy

```html
<!DOCTYPE html>
<html lang="en">
<head>
<meta charset="utf-8">
<title>TrailBirch Business Card</title>
<link rel="stylesheet" href="https://fonts.googleapis.com/css2?family=Montserrat:wght@600&family=Arimo:wght@400;700&display=swap">
<style>
  :root {
    --backdrop: #ece7df;
    --card: #ffffff;
    --card-shadow: rgba(60, 45, 30, 0.18);
    --brand-blue: #1a6fc2;
    --brand-soft: #a9b8e6;
    --accent-red: #f0401e;
    --ink: #111111;
    --icon: #1a6fc2;
  }
  * { box-sizing: border-box; margin: 0; padding: 0; }
  html, body {
    width: 1200px; height: 1000px; overflow: hidden;
    background: var(--backdrop);
  }
  .sheet {
    width: 1200px; height: 1000px;
    display: flex; flex-direction: column;
    align-items: center; justify-content: center; gap: 60px;
  }
  .card {
    position: relative;
    width: 700px; height: 400px;
    background: var(--card);
    box-shadow: 0 10px 30px var(--card-shadow);
    overflow: hidden;
  }
  /* Front */
  .card--front { display: flex; align-items: center; justify-content: center; }
  .brand-front {
    font-family: "Montserrat", sans-serif;
    font-weight: 600; font-size: 84px; letter-spacing: 1px;
    color: var(--brand-soft);
  }
  /* Back */
  .name-bar {
    position: absolute; left: 0; top: 90px;
    width: 330px; height: 48px;
    background: var(--brand-blue); color: #fff;
    font-family: "Arimo", sans-serif; text-align: center;
    padding-top: 6px;
  }
  .name-bar .person { font-weight: 700; font-size: 22px; line-height: 24px; display: block; }
  .name-bar .role { font-size: 11px; line-height: 12px; display: block; padding-left: 60px; }
  .stripe { position: absolute; top: 138px; height: 210px; width: 14px; }
  .stripe--red { left: 0; background: var(--accent-red); }
  .stripe--blue { left: 14px; width: 12px; background: var(--brand-blue); }
  .contact-list {
    position: absolute; left: 40px; top: 150px;
    list-style: none;
    font-family: "Arimo", sans-serif; font-weight: 700; font-size: 17px; color: var(--ink);
  }
  .contact-list li { display: flex; align-items: center; gap: 10px; height: 38px; white-space: nowrap; }
  .contact-list svg { width: 24px; height: 24px; flex: none; }
  .brand-back {
    position: absolute; left: 420px; top: 110px;
    font-family: "Montserrat", sans-serif;
    font-weight: 600; font-size: 40px; color: var(--brand-blue);
  }
</style>
</head>
<body>
<main class="sheet">
  <section class="card card--front">
    <span class="brand-front">TrailBirch</span>
  </section>

  <section class="card card--back">
    <div class="name-bar">
      <span class="person">Ross Dalby</span>
      <span class="role">CEO</span>
    </div>
    <div class="stripe stripe--red"></div>
    <div class="stripe stripe--blue"></div>
    <ul class="contact-list">
      <li>
        <svg viewBox="0 0 24 24" aria-hidden="true"><path fill="var(--icon)" d="M3 8c0-2 2-4 9-4s9 2 9 4v2h-5V8H8v2H3zM6 12h12l2 8H4z"/><circle cx="12" cy="16" r="2.2" fill="#fff"/></svg>
        555-304-7192
      </li>
      <li>
        <svg viewBox="0 0 24 24" aria-hidden="true"><rect x="2" y="5" width="20" height="14" fill="var(--icon)"/><path d="M2 5l10 8 10-8" fill="none" stroke="#fff" stroke-width="1.6"/></svg>
        Dalbycrew@TrailBirch.example
      </li>
      <li>
        <svg viewBox="0 0 24 24" aria-hidden="true" fill="none" stroke="var(--icon)" stroke-width="1.6"><circle cx="12" cy="12" r="9.5"/><ellipse cx="12" cy="12" rx="4.5" ry="9.5"/><path d="M2.5 12h19M4.5 7h15M4.5 17h15"/></svg>
        www.TrailBirch.example
      </li>
      <li>
        <svg viewBox="0 0 24 24" aria-hidden="true"><rect x="2" y="2" width="20" height="20" fill="var(--icon)"/></svg>
        www.FriendLoop.example/TrailBirch
      </li>
      <li>
        <svg viewBox="0 0 24 24" aria-hidden="true"><rect x="2" y="2" width="20" height="20" fill="var(--icon)"/></svg>
        @dalby_ross
      </li>
    </ul>
    <span class="brand-back">TrailBirch</span>
  </section>
</main>
</body>
</html>
```